Fall/Winter HVAC billboard

Looking to update our billboard for the heating season.
Want to $ave on heating bills
Consider it done!

Target Market(s)

Commuters - homeowners

Industry/Entity Type

HVAC - heating and Air conditioning

```html
<!DOCTYPE html>
<html lang="en">
<head>
<meta charset="utf-8">
<title>Heating Season Billboard</title>
<link rel="stylesheet" href="https://fonts.googleapis.com/css2?family=Bowlby+One&family=Open+Sans:wght@700;800&family=Noto+Serif:wght@700&display=swap">
<style>
  :root {
    --ink: #231f20;
    --gold: #fbb125;
    --sky: #009ddc;
    --white: #ffffff;
    --photo-light: #f1f2f3;
    --photo-mid: #d9dcde;
    --hero-gold: #e9a826;
    --hero-blue: #2d8fd6;
  }
  * { margin: 0; padding: 0; box-sizing: border-box; }
  html, body { width: 1200px; height: 274px; overflow: hidden; background: var(--ink); }
  .billboard {
    position: relative;
    width: 1200px;
    height: 274px;
    background: var(--ink);
    overflow: hidden;
  }
  .brand {
    position: absolute;
    left: 26px;
    top: 30px;
    display: flex;
    align-items: center;
    gap: 10px;
    font-family: "Open Sans", sans-serif;
    font-weight: 800;
    color: var(--sky);
  }
  .brand-dot {
    width: 46px;
    height: 46px;
    border-radius: 50%;
    background: var(--sky);
    flex: none;
  }
  .brand-name { display: flex; flex-direction: column; line-height: 1.05; }
  .brand-name .main { font-size: 36px; letter-spacing: 1px; }
  .brand-name .sub { font-size: 14px; }
  .hero-art {
    position: absolute;
    left: 14px;
    top: 118px;
    width: 262px;
    height: 156px;
    border-radius: 40px 60px 0 0;
    background: linear-gradient(135deg, var(--hero-gold) 0%, var(--hero-blue) 55%, var(--hero-gold) 100%);
  }
  .headline {
    position: absolute;
    left: 283px;
    top: 22px;
    color: var(--gold);
  }
  .headline .line-one {
    font-family: "Bowlby One", sans-serif;
    font-size: 54px;
    line-height: 1;
    letter-spacing: 1px;
    display: block;
  }
  .headline .line-two {
    font-family: "Open Sans", sans-serif;
    font-weight: 800;
    font-size: 44px;
    line-height: 1;
    margin-top: 12px;
    display: block;
    letter-spacing: 0.5px;
  }
  .tagline {
    position: absolute;
    left: 284px;
    top: 130px;
    font-family: "Noto Serif", serif;
    font-weight: 700;
    font-size: 45px;
    color: var(--white);
    letter-spacing: 1.5px;
    line-height: 1;
  }
  .call-band {
    position: absolute;
    left: 268px;
    top: 194px;
    width: 520px;
    height: 62px;
    background: var(--sky);
  }
  .call-band .phone {
    position: absolute;
    left: 14px;
    top: 6px;
    font-family: "Open Sans", sans-serif;
    font-weight: 800;
    font-size: 43px;
    color: var(--white);
    letter-spacing: 2px;
    line-height: 1.15;
    white-space: nowrap;
  }
  .product-photo {
    position: absolute;
    left: 730px;
    top: 0;
    width: 470px;
    height: 274px;
  }
</style>
</head>
<body>
  <main class="billboard">
    <div class="brand">
      <span class="brand-dot"></span>
      <span class="brand-name">
        <span class="main">VANTOR</span>
        <span class="sub">Heating &amp; Air Conditioning</span>
      </span>
    </div>

    <div class="hero-art" role="img" aria-label="Illustrated superhero technician in a blue suit and gold cape flying forward with fist outstretched"></div>

    <h1 class="headline">
      <span class="line-one">WANT TO $AVE</span>
      <span class="line-two">ON HEATING BILLS</span>
    </h1>

    <p class="tagline">Consider it done!</p>

    <div class="call-band">
      <span class="phone">CALL 203-555-0148</span>
    </div>

    <svg class="product-photo" viewBox="0 0 470 274" role="img" aria-label="Photo of a hand turning a white thermostat dial with a glowing blue display reading SAVE">
      <defs>
        <linearGradient id="photoTone" x1="0" y1="0" x2="1" y2="1">
          <stop offset="0" stop-color="var(--photo-light)"/>
          <stop offset="0.6" stop-color="var(--photo-mid)"/>
          <stop offset="1" stop-color="#bfc3c6"/>
        </linearGradient>
      </defs>
      <path d="M12 0 H470 V274 H44 C58 230 30 200 46 160 C60 120 30 90 40 50 C46 25 20 12 12 0 Z" fill="url(#photoTone)"/>
    </svg>
  </main>
</body>
</html>
```